ShelfNook Template

Hi Guys,

I have just completed a logo design with Pixel Gather and I am very happy with what I have seen so far. Next I would like to create a template for the site that will be skinned into a DNN skin.

Our goal with ShelfNook is to create a site were people can register and buy a e-commerce site from us. The site needs to match the logo color scheme and entice people to register. The site needs to be clear on what they are receiving and make sure that the registration process is easily accessible. our target market is the Joe Soup's that want to create an online presence and sell their products.

I'm excited to see what you guys are going to come up with.

Regards

Pieter
Updates

Hi all,

Thank you for your inputs, It was hard to choose a template as I feel that so many of them where so good.

Well done.

Regards

Pieter Vosloo

Industry/Entity Type

E-Commerce

```html
<!DOCTYPE html>
<html lang="en">
<head>
<meta charset="utf-8">
<title>ShelfNook – Online Store Builder</title>
<link href="https://fonts.googleapis.com/css2?family=Titillium+Web:wght@300;400;600;700&family=Open+Sans:wght@400;600&family=Lobster&family=Pacifico&display=swap" rel="stylesheet">
<style>
:root{
  --navy:#0d2f6b;
  --navy-ink:#0b2a5e;
  --hero-top:#0a1f4e;
  --hero-glow:#1f5cb0;
  --orange:#f26a21;
  --cyan:#5fd0f5;
  --white:#ffffff;
  --grey-bg:#efefef;
  --grey-card:#e6e6e6;
  --text:#6d6d6d;
  --text-light:#9a9a9a;
  --footer-link:#9fc2ee;
  --footer-bar:#061638;
}
*{box-sizing:border-box;margin:0;padding:0}
html,body{width:793px;height:1200px;overflow:hidden}
body{position:relative;background:var(--white);font-family:"Open Sans",sans-serif;color:var(--text)}

/* header */
.site-header{position:absolute;left:0;top:0;width:793px;height:54px;background:var(--white)}
.brand{position:absolute;left:116px;top:13px;display:flex;align-items:center;gap:7px}
.brand-mark{width:22px;height:22px;background:var(--navy);border-radius:4px}
.brand-name{font-family:"Titillium Web",sans-serif;font-weight:700;font-size:27px;color:var(--orange);line-height:1}
.main-nav a{position:absolute;top:24px;font-family:"Titillium Web",sans-serif;font-weight:700;font-size:10px;color:var(--navy-ink);text-decoration:none;letter-spacing:.3px}
.main-nav a.active{top:21px;left:349px;width:47px;height:20px;line-height:20px;text-align:center;background:var(--navy);color:var(--white);border-radius:2px}

/* hero */
.hero{position:absolute;left:0;top:54px;width:793px;height:327px;
  background:radial-gradient(ellipse 180px 200px at 0 300px,var(--hero-glow),transparent 80%),
             linear-gradient(180deg,var(--hero-top),#0f3272 55%,#123a80)}
.hero-kicker{position:absolute;top:13px;width:100%;text-align:center;font-family:"Titillium Web",sans-serif;font-weight:300;font-size:15px;line-height:20px;color:var(--white)}
.hero-title{position:absolute;top:32px;width:100%;text-align:center;font-family:"Titillium Web",sans-serif;font-weight:300;font-size:35px;line-height:1;color:var(--cyan);letter-spacing:.5px}
.hero-sub{position:absolute;top:64px;width:100%;text-align:center;font-family:"Titillium Web",sans-serif;font-weight:400;font-size:20px;line-height:1;color:var(--white);letter-spacing:2px}
.hero-note{position:absolute;top:89px;width:100%;text-align:center;font-size:7.5px;color:#bcd6ff}
.hero-visual{position:absolute;left:187px;top:115px;width:407px;height:212px;border-radius:10px 10px 0 0;
  background:linear-gradient(160deg,#2a3140,#3b4032 50%,#6a6f74)}

/* call to action band */
.cta-band{position:absolute;left:0;top:381px;width:793px;height:72px;background:var(--orange)}
.cta-text{position:absolute;left:117px;top:24px;font-family:"Pacifico",cursive;font-size:12.5px;line-height:20px;color:var(--white);white-space:nowrap}
.cta-button{position:absolute;left:538px;top:27px;width:136px;height:29px;border-radius:15px;background:var(--navy);border:2px solid #2c5aa8;
  color:var(--white);font-family:"Titillium Web",sans-serif;font-weight:700;font-size:11px;line-height:25px;text-align:center;text-decoration:none}

/* benefits */
.benefits{position:absolute;left:0;top:453px;width:793px;height:142px;background:var(--white)}
.benefit{position:absolute;top:17px;width:150px;text-align:center}
.benefit-icon{width:50px;height:50px;border-radius:50%;background:var(--navy);margin:0 auto;display:flex;align-items:center;justify-content:center;box-shadow:0 0 0 2px #c9d4e8}
.benefit h3{margin-top:14px;font-family:"Titillium Web",sans-serif;font-weight:700;font-size:10px;color:var(--navy-ink)}
.benefit p{margin-top:3px;font-size:7px;line-height:1.35;color:var(--text-light);padding:0 6px}

/* services */
.services{position:absolute;left:0;top:595px;width:793px;height:286px;background:var(--grey-bg)}
.section-title{position:absolute;width:100%;text-align:center;font-family:"Lobster",cursive;font-size:22px;color:var(--navy-ink)}
.service{position:absolute;width:172px;height:94px;border:1px dashed #c9c9c9;padding:9px 9px 0}
.service-head{display:flex;align-items:center;gap:7px;height:26px}
.service-head svg{flex:none}
.service h4{font-family:"Titillium Web",sans-serif;font-weight:700;font-size:9.5px;color:var(--navy-ink);white-space:nowrap}
.service p{margin-top:6px;font-size:7px;line-height:1.3;color:var(--text-light);text-align:justify}
.services-notch{position:absolute;left:391px;top:280px;width:12px;height:12px;background:var(--white);transform:rotate(45deg)}

/* testimonials */
.testimonials{position:absolute;left:0;top:881px;width:793px;height:133px;background:var(--white)}
.testimonial{position:absolute;top:46px;width:276px;height:75px;background:var(--grey-card)}
.avatar{position:absolute;left:10px;top:10px;width:30px;height:30px;border-radius:50%;background:linear-gradient(135deg,#b08a6a,#6b4a38);border:2px solid var(--white)}
.testimonial p{position:absolute;left:48px;top:10px;right:12px;font-size:7px;line-height:1.3;color:var(--text);text-align:justify}
.testimonial .who{position:absolute;right:12px;top:46px;font-size:7.5px;color:var(--navy-ink)}
.testimonial .who span{display:block;color:var(--orange)}

/* footer */
.site-footer{position:absolute;left:0;top:1014px;width:793px;height:159px;
  background:linear-gradient(180deg,#0a2a66,#0d3a86 60%,#0a2e70)}
.footer-col{position:absolute;top:30px}
.footer-col h5{font-family:"Titillium Web",sans-serif;font-weight:700;font-size:9.5px;color:var(--white);margin-bottom:6px;letter-spacing:.3px}
.footer-col a{display:block;font-size:7px;line-height:11.2px;color:var(--footer-link);text-decoration:none}
.footer-contact p{width:176px;font-size:7px;line-height:1.3;color:var(--footer-link)}
.footer-input{position:absolute;left:501px;top:82px;width:175px;height:17px;background:#9ec3ee}
.footer-subscribe{position:absolute;left:613px;top:105px;width:63px;height:19px;background:var(--orange);border-radius:2px;color:var(--white);
  font-family:"Titillium Web",sans-serif;font-weight:700;font-size:8.5px;line-height:19px;text-align:center}
.footer-bar{position:absolute;left:0;top:1173px;width:793px;height:27px;background:var(--footer-bar)}
.footer-bar .copy{position:absolute;left:117px;top:9px;font-size:7px;color:#c7d6ee}
.footer-bar nav{position:absolute;right:117px;top:9px;display:flex;gap:9px}
.footer-bar nav a{font-size:7px;color:#c7d6ee;text-decoration:none}
</style>
</head>
<body>

<header class="site-header">
  <div class="brand"><span class="brand-mark"></span><span class="brand-name">ShelfNook</span></div>
  <nav class="main-nav">
    <a class="active" href="#">HOME</a>
    <a href="#" style="left:408px">FEATURES</a>
    <a href="#" style="left:465px">PRICING</a>
    <a href="#" style="left:513px">ABOUT US</a>
    <a href="#" style="left:571px">SHOWCASE</a>
    <a href="#" style="left:631px">CONTACT US</a>
  </nav>
</header>

<section class="hero">
  <p class="hero-kicker">Our firm's mission is to listen to clients</p>
  <h1 class="hero-title">EVERYTHING YOU NEED TO</h1>
  <h2 class="hero-sub">CREATE A SUCESSFUL ONLINE STORE</h2>
  <p class="hero-note">24/7 monitoring system monitoring every role on every server and desktop. Proactively fixing problems before the users know there is an issue.</p>
  <div class="hero-visual" role="img" aria-label="Product photo: laptop displaying a sample online store, with a milkshake glass beside it"></div>
</section>

<section class="cta-band">
  <p class="cta-text">Start building powerful, professional, easy to use websites and online stores</p>
  <a class="cta-button" href="#">CLICK TO REGISTER HERE</a>
</section>

<section class="benefits">
  <div class="benefit" style="left:94px">
    <div class="benefit-icon"><svg width="26" height="22" viewBox="0 0 26 22"><rect x="2" y="2" width="22" height="14" rx="1" fill="none" stroke="#fff" stroke-width="2"/><path d="M9 20h8M13 16v4" stroke="#fff" stroke-width="2"/><path d="M10 6l6 5-3 .5-1 2.5z" fill="#fff"/></svg></div>
    <h3>EASY TO USE &amp; FLEXIBLE</h3>
    <p>Sed ut perspiciatis unde omnis iste natus error sit voluptatem accusan-tium doloremque laudantium, totam rem aperiam.</p>
  </div>
  <div class="benefit" style="left:247px">
    <div class="benefit-icon"><svg width="26" height="22" viewBox="0 0 26 22"><path d="M8 9l5-6 5 6" fill="none" stroke="#fff" stroke-width="2"/><path d="M2 9h22l-3 11H5z" fill="#fff"/><path d="M9 12v5M13 12v5M17 12v5" stroke="#0d2f6b" stroke-width="1.6"/></svg></div>
    <h3>POWERFUL ECOMMERCE</h3>
    <p>Sed ut perspiciatis unde omnis iste natus error sit voluptatem accusan-tium doloremque laudantium, totam rem aperiam.</p>
  </div>
  <div class="benefit" style="left:397px">
    <div class="benefit-icon"><svg width="24" height="24" viewBox="0 0 24 24"><path d="M4 20l3-8 9-9 5 5-9 9z" fill="#fff"/><path d="M4 20l4-1-3-3z" fill="#0d2f6b"/></svg></div>
    <h3>AMAZING DESIGNS</h3>
    <p>Sed ut perspiciatis unde omnis iste natus error sit voluptatem accusan-tium doloremque laudantium, totam rem aperiam.</p>
  </div>
  <div class="benefit" style="left:550px">
    <div class="benefit-icon"><svg width="26" height="22" viewBox="0 0 26 22"><path d="M2 4h8l2 3h12v13H2z" fill="#fff"/><path d="M10 15l5-5M9 13l-1 1a2 2 0 003 3l1-1M16 12l1-1a2 2 0 00-3-3l-1 1" fill="none" stroke="#0d2f6b" stroke-width="1.6"/></svg></div>
    <h3>PACKED WITH FEATURES</h3>
    <p>Sed ut perspiciatis unde omnis iste natus error sit voluptatem accusan-tium doloremque laudantium, totam rem aperiam.</p>
  </div>
</section>

<section class="services">
  <h2 class="section-title" style="top:12px">We Provide You</h2>

  <div class="service" style="left:116px;top:54px">
    <div class="service-head"><svg width="24" height="24" viewBox="0 0 24 24"><rect x="2" y="6" width="14" height="16" fill="#2c6fc9"/><path d="M8 18l12-14 3 2-12 14-4 1z" fill="#e23b2e"/></svg><h4>EASY CUSTOMIZATION</h4></div>
    <p>Sed ut perspiciatis unde omnis iste natus error sit voluptatem accusantium doloremque laudantium, totam rem aperiam, eaque ipsa quae ab illo inventore veritatis et quasi architecto beatae vitae dicta sunt explicabo.</p>
  </div>
  <div class="service" style="left:310px;top:54px">
    <div class="service-head"><svg width="24" height="24" viewBox="0 0 24 24"><circle cx="12" cy="12" r="9" fill="none" stroke="#2c6fc9" stroke-width="4" stroke-dasharray="3 2.2"/><circle cx="12" cy="12" r="6" fill="#2c6fc9"/><circle cx="12" cy="12" r="3" fill="#f2c14e"/></svg><h4>SOLID FRAMEWORK</h4></div>
    <p>Sed ut perspiciatis unde omnis iste natus error sit voluptatem accusantium doloremque laudantium, totam rem aperiam, eaque ipsa quae ab illo inventore veritatis et quasi architecto beatae vitae dicta sunt explicabo.</p>
  </div>
  <div class="service" style="left:502px;top:54px">
    <div class="service-head"><svg width="24" height="24" viewBox="0 0 26 24"><rect x="2" y="3" width="18" height="17" rx="2" fill="#fff" stroke="#bbb"/><rect x="2" y="3" width="18" height="5" fill="#e23b2e"/><circle cx="19" cy="16" r="6" fill="#f2a83a"/><path d="M16 16l2 2 4-4" stroke="#fff" stroke-width="1.6" fill="none"/></svg><h4>NEW THEMES EVERY MONTH</h4></div>
    <p>Sed ut perspiciatis unde omnis iste natus error sit voluptatem accusantium doloremque laudantium, totam rem aperiam, eaque ipsa quae ab illo inventore veritatis et quasi architecto beatae vitae dicta sunt explicabo.</p>
  </div>

  <div class="service" style="left:116px;top:167px">
    <div class="service-head"><svg width="24" height="24" viewBox="0 0 24 24"><rect x="3" y="2" width="12" height="18" fill="#d9dde3" stroke="#999"/><circle cx="15" cy="16" r="7" fill="#3aa63a"/><path d="M13 12.5v7l5.5-3.5z" fill="#fff"/></svg><h4>NEQUE PORRO QUISQUAM</h4></div>
    <p>Sed ut perspiciatis unde omnis iste natus error sit voluptatem accusantium doloremque laudantium, totam rem aperiam, eaque ipsa quae ab illo inventore veritatis et quasi architecto beatae vitae dicta sunt explicabo.</p>
  </div>
  <div class="service" style="left:310px;top:167px">
    <div class="service-head"><svg width="24" height="24" viewBox="0 0 24 24"><circle cx="12" cy="12" r="10" fill="#555"/><circle cx="12" cy="12" r="6" fill="none" stroke="#fff" stroke-width="2"/><path d="M12 8v4l3 2" stroke="#fff" stroke-width="2" fill="none"/></svg><h4>QUIS AUTEM VEL EUM</h4></div>
    <p>Sed ut perspiciatis unde omnis iste natus error sit voluptatem accusantium doloremque laudantium, totam rem aperiam, eaque ipsa quae ab illo inventore veritatis et quasi architecto beatae vitae dicta sunt explicabo.</p>
  </div>
  <div class="service" style="left:502px;top:167px">
    <div class="service-head"><svg width="24" height="24" viewBox="0 0 24 24"><circle cx="12" cy="12" r="8" fill="none" stroke="#e8532f" stroke-width="5" stroke-dasharray="6.3 6.3"/><circle cx="12" cy="12" r="10.5" fill="none" stroke="#ccc" stroke-width="1"/></svg><h4>SED UT PERSPICIATIS</h4></div>
    <p>Sed ut perspiciatis unde omnis iste natus error sit voluptatem accusantium doloremque laudantium, totam rem aperiam, eaque ipsa quae ab illo inventore veritatis et quasi architecto beatae vitae dicta sunt explicabo.</p>
  </div>
  <div class="services-notch"></div>
</section>

<section class="testimonials">
  <h2 class="section-title" style="top:11px">Our Client Testimonials</h2>
  <figure class="testimonial" style="left:115px">
    <div class="avatar" role="img" aria-label="Portrait photo of the client"></div>
    <p>Sed ut perspiciatis unde omnis iste natus error sit voluptatem accusantium doloremque laudantium, totam rem aperiam, eaque ipsa quae ab illo inventore veritatis et quasi architecto beatae vitae dicta sunt explicabo.</p>
    <figcaption class="who">Mara Olsen<span>USA</span></figcaption>
  </figure>
  <figure class="testimonial" style="left:403px">
    <div class="avatar" role="img" aria-label="Portrait photo of the client"></div>
    <p>Sed ut perspiciatis unde omnis iste natus error sit voluptatem accusantium doloremque laudantium, totam rem aperiam, eaque ipsa quae ab illo inventore veritatis et quasi architecto beatae vitae dicta sunt explicabo.</p>
    <figcaption class="who">Mara Olsen<span>USA</span></figcaption>
  </figure>
</section>

<footer class="site-footer">
  <div class="footer-col" style="left:117px"><h5>PRODUCT</h5>
    <a href="#">About Us</a><a href="#">Our Blog</a><a href="#">Pricing</a><a href="#">Our Themes</a><a href="#">Features</a><a href="#">Terms and Conditions</a></div>
  <div class="footer-col" style="left:217px"><h5>MARKETPLACE</h5>
    <a href="#">Support Forum</a><a href="#">Documentation</a><a href="#">FAQ</a><a href="#">Customization</a><a href="#">Installation Service</a><a href="#">Video Tutorials</a><a href="#">Support Policy</a><a href="#">Contact Us</a></div>
  <div class="footer-col" style="left:323px"><h5>SUPPORT</h5>
    <a href="#">Showcase</a><a href="#">Press</a><a href="#">Partners</a><a href="#">Hosting</a><a href="#">Affiliates</a><a href="#">Promotions</a><a href="#">Features</a></div>
  <div class="footer-col" style="left:413px"><h5>ABOUT US</h5>
    <a href="#">News</a><a href="#">New Themes</a><a href="#">Contests</a><a href="#">Theme Concepts</a><a href="#">Freebies</a><a href="#">Highlight</a><a href="#">Promotions</a><a href="#">Tips &amp; Advice</a></div>
  <div class="footer-col footer-contact" style="left:501px"><h5>GET IN TOUCH WITH US</h5>
    <p>We would love to hear about you, be part of our community come join us, we will have so much fun! We have all kinds of gifts and cool stuff for you!</p></div>
  <div class="footer-input"></div>
  <div class="footer-subscribe">SUBSCRIBE</div>
</footer>

<div class="footer-bar">
  <p class="copy">Copyright © 2013 - Shelfnook.com Premium Themes - All rights reserved.</p>
  <nav><a href="#">Home</a><a href="#">Features</a><a href="#">Terms &amp; Conditions</a><a href="#">FAQ</a><a href="#">Contact</a></nav>
</div>

</body>
</html>
```